I need a poster/ad for my St. Patrick's Day Party called Bluff Corwin's Day. The poster needs to be easy to read and entice people to come to our bar for a party.

Copy Should Say:

Bluff Corwin's Day!
Saturday, March 17, 2018
Live Music by the VELVET ROVERS
Free food! drink specials! No cover charge!
9pm, 21+
Harlow Creek Tavern
Rt.58, Hillsdale, NY

Target Market(s)

People who like to drink and party. Ages 21-50+

Font styles to use
Sans Serif

Requirements
Must have
• Must look like the American holiday 'St. Patrick's day". The band is called "Velvet Rovers" and they should be very prominent on the flyer because they are the big attraction. Green is the main color of St. Patrick's Day.
Nice to have
• If you have seen our past winning designs, my favorites are always the ones that feature our famous building, the Harlow Creek Tavern.
• If you want to learn more about us, our website is www.harlowcreektavern.com

```html
<!DOCTYPE html>
<html lang="en">
<head>
<meta charset="utf-8">
<title>Bluff Corwin's Day! – Harlow Creek Tavern</title>
<link href="https://fonts.googleapis.com/css2?family=Montserrat:ital,wght@1,800;1,900&family=Raleway:wght@600;800&family=Ultra&display=swap" rel="stylesheet">
<style>
  :root {
    --orange-top: #e99a24;
    --orange-mid: #e5c11f;
    --orange-low: #d8822a;
    --green-dark: #1b5e20;
    --green: #2e8b2e;
    --green-bright: #46b13e;
    --green-pale: #b5d48a;
    --ink: #161616;
    --paper: #ffffff;
    --footer: #0c0f0c;
  }
  * { margin: 0; padding: 0; box-sizing: border-box; }
  html, body { width: 970px; height: 1200px; overflow: hidden; background: #ffffff; }
  .poster { position: relative; width: 970px; height: 1200px; background: var(--paper); overflow: hidden; }

  .header-wave { position: absolute; left: 0; top: 0; width: 970px; height: 520px; }

  .festive-art {
    position: absolute; left: 0; top: 14px; width: 420px; height: 480px;
    background: radial-gradient(ellipse at 45% 55%, #3aa53a 0%, #23802a 45%, rgba(230,180,40,0.85) 75%, rgba(233,154,36,0) 100%);
    border-radius: 0 0 50% 0 / 0 0 30% 0;
  }

  .event-title {
    position: absolute; right: 34px; top: 96px; text-align: right;
    font-family: "Montserrat", sans-serif; font-style: italic; font-weight: 900;
    color: var(--green);
    -webkit-text-stroke: 3px #ffffff; paint-order: stroke fill;
    text-shadow: 0 3px 0 var(--green-dark);
    line-height: 0.95; letter-spacing: -1px;
  }
  .event-title .line-1 { display: block; font-size: 108px; }
  .event-title .line-2 { display: block; font-size: 76px; margin-top: 10px; }
  .event-title .line-3 { display: block; font-size: 76px; margin-top: 6px; }

  .lineup { position: absolute; left: 0; top: 538px; width: 970px; text-align: center; }
  .lineup-intro {
    font-family: "Raleway", sans-serif; font-weight: 800; font-size: 30px;
    color: var(--green-dark); letter-spacing: 0.3px;
  }
  .band-name {
    font-family: "Ultra", serif; font-size: 120px; line-height: 118px;
    color: var(--ink); margin-top: 8px;
  }

  .details { position: absolute; left: 99px; top: 872px; }
  .details .label {
    font-family: "Raleway", sans-serif; font-weight: 800; font-size: 31px;
    color: var(--green-dark); line-height: 38px;
  }
  .details .info {
    font-family: "Ultra", serif; font-size: 27px; line-height: 38px; color: var(--ink);
  }
  .details .gap { margin-top: 16px; }

  .venue-mark {
    position: absolute; left: 656px; top: 880px; width: 200px; height: 190px;
    display: flex; flex-direction: column; align-items: center; justify-content: center; gap: 12px;
  }
  .venue-mark .dot { width: 34px; height: 34px; border-radius: 50%; background: var(--ink); }
  .venue-mark .name {
    font-family: "Raleway", sans-serif; font-weight: 800; font-size: 26px;
    color: var(--ink); text-align: center; line-height: 30px;
  }

  .footer {
    position: absolute; left: 0; bottom: 0; width: 970px; height: 90px;
    background: radial-gradient(ellipse at 50% 120%, #1f4a1c 0%, var(--footer) 70%);
    display: flex; align-items: center; justify-content: center;
    font-family: "Raleway", sans-serif; font-weight: 600; font-size: 31px; color: #ffffff;
  }
</style>
</head>
<body>
<main class="poster">
  <svg class="header-wave" viewBox="0 0 970 520" aria-hidden="true">
    <defs>
      <linearGradient id="headerGlow" x1="0" y1="0" x2="0" y2="1">
        <stop offset="0" stop-color="#e99a24"/>
        <stop offset="0.55" stop-color="#e5c11f"/>
        <stop offset="1" stop-color="#d8822a"/>
      </linearGradient>
    </defs>
    <path d="M0 520 L0 470 C200 430 380 420 560 440 C760 462 880 470 970 360 L970 520 Z" fill="#1b5e20"/>
    <path d="M0 0 H970 V360 C880 450 760 455 560 425 C380 400 200 410 0 455 Z" fill="#b5d48a"/>
    <path d="M0 0 H970 V345 C880 432 760 438 560 410 C380 385 200 395 0 440 Z" fill="#d8822a"/>
    <path d="M0 0 H970 V330 C880 418 760 420 560 395 C380 370 200 380 0 425 Z" fill="url(#headerGlow)"/>
  </svg>

  <div class="festive-art" role="img" aria-label="Green leprechaun hat on a pot of gold coins with shamrocks and a golden horseshoe"></div>

  <h1 class="event-title">
    <span class="line-1">BLUFF</span>
    <span class="line-2">CORWIN'S</span>
    <span class="line-3">DAY!</span>
  </h1>

  <section class="lineup">
    <p class="lineup-intro">LIVE MUSIC BY THE</p>
    <h2 class="band-name">Velvet<br>Rovers</h2>
  </section>

  <section class="details">
    <p class="label">SATURDAY</p>
    <p class="info">MARCH 17, 2018</p>
    <p class="label gap">FREE FOOD!</p>
    <p class="info">Drink Specials!</p>
    <p class="info">No Cover Charge! 9pm, 21+</p>
  </section>

  <div class="venue-mark">
    <span class="dot"></span>
    <span class="name">Harlow Creek<br>Tavern</span>
  </div>

  <footer class="footer">Harlow Creek Tavern Rt.58, Hillsdale, NY</footer>
</main>
</body>
</html>
```